Business Card Design Project

Need business card for new non profit organization that includes the attached logo in some form.
with this information
Name: Michael Dorrance Pilbeam
Title: President & Founder
A: P.O. Box 51607, Portland, Oregon, 97214-5160
E: mike@dorrancetrust.org
E: mike@mikepilbeam.com
P: 1.971.555.0172

Industry/Entity Type
Non Profit

```html
<!DOCTYPE html>
<html lang="en">
<head>
<meta charset="utf-8">
<title>Dorrance Trust – Business Card</title>
<link rel="stylesheet" href="https://fonts.googleapis.com/css2?family=Cabin:wght@400;600&display=swap">
<style>
  :root {
    --card-bg: #ffffff;
    --ink: #58595b;
    --brand-purple: #3a3282;
    --brand-yellow: #fff000;
    --brand-navy: #1f3a7a;
    --mark-grey: #dcdcdc;
  }
  html, body {
    margin: 0;
    padding: 0;
    overflow: hidden;
    background: var(--card-bg);
  }
  .card {
    position: relative;
    width: 1200px;
    height: 686px;
    overflow: hidden;
    background: var(--card-bg);
    font-family: "Cabin", "Gill Sans", sans-serif;
    color: var(--ink);
  }
  .card__shapes {
    position: absolute;
    inset: 0;
    width: 1200px;
    height: 686px;
  }
  .holder {
    position: absolute;
    left: 46px;
    top: 36px;
    margin: 0;
  }
  .holder__name {
    margin: 0;
    font-size: 44px;
    font-weight: 400;
    line-height: 1;
    letter-spacing: 0.2px;
  }
  .holder__title {
    margin: 14px 0 0;
    font-size: 28px;
    font-weight: 400;
    line-height: 1;
  }
  .org-name {
    position: absolute;
    left: 780px;
    top: 98px;
    display: flex;
    align-items: center;
    gap: 14px;
    font-size: 38px;
    font-weight: 600;
    color: var(--brand-navy);
    line-height: 1;
  }
  .org-name__dot {
    width: 26px;
    height: 26px;
    border-radius: 50%;
    background: var(--brand-navy);
  }
  .contact {
    position: absolute;
    left: 682px;
    top: 248px;
    margin: 0;
    font-style: normal;
    line-height: 1;
  }
  .contact__address {
    font-size: 35px;
    line-height: 44px;
  }
  .contact__email {
    font-size: 29px;
    line-height: 44px;
  }
  .contact__phone {
    font-size: 37px;
    line-height: 48px;
  }
</style>
</head>
<body>
  <main class="card">
    <svg class="card__shapes" viewBox="0 0 1051 600" preserveAspectRatio="none" aria-hidden="true">
      <defs>
        <linearGradient id="band-fade" x1="0" y1="0" x2="1" y2="0">
          <stop offset="0" stop-color="#ffffff"/>
          <stop offset="0.4" stop-color="#fff000"/>
          <stop offset="1" stop-color="#fff000"/>
        </linearGradient>
        <linearGradient id="pattern-glow" x1="0" y1="0" x2="1" y2="0">
          <stop offset="0" stop-color="#fff7a0"/>
          <stop offset="1" stop-color="#fff58a"/>
        </linearGradient>
      </defs>
      <rect class="band-bottom" x="330" y="437" width="721" height="163" fill="url(#band-fade)"/>
      <polygon class="stripe-yellow" points="0,290 135,408 178,420 184,448 330,600 185,600 0,418" fill="var(--brand-yellow)"/>
      <polygon class="stripe-purple" points="0,120 490,600 345,600 195,445 190,415 150,405 0,258" fill="var(--brand-purple)"/>
    </svg>

    <svg class="card__shapes" viewBox="0 0 1051 600" preserveAspectRatio="none">
      <rect class="pattern-area" x="552" y="458" width="450" height="118" rx="6" fill="url(#pattern-glow)" opacity="0.8" role="img" aria-label="Rows of pale diamond shapes"/>
      <rect class="emblem-area" x="292" y="152" width="190" height="178" rx="10" fill="var(--mark-grey)" opacity="0.55" role="img" aria-label="Faint grey community emblem"/>
    </svg>

    <header class="holder">
      <h1 class="holder__name">Michael Dorrance Pilbeam</h1>
      <p class="holder__title">President &amp; Founder</p>
    </header>

    <div class="org-name">
      <span class="org-name__dot"></span>
      <span>Dorrance Trust</span>
    </div>

    <address class="contact">
      <div class="contact__address">P.O. Box 51607, Portland,<br>Oregon, 97214-5160</div>
      <div class="contact__email">mike@dorrancetrust.org</div>
      <div class="contact__email">mike@mikepilbeam.com</div>
      <div class="contact__phone">1.971.555.0172</div>
    </address>
  </main>
</body>
</html>
```